Harbortail Keepers Florida Retractable Banner Design

Looking for a fresh, modern, eye catching yet informative retractable banner design for our vendor booth events.

Our color scheme is teal, dark yellow, black, and white

Would like to include our services of Overnights, Pop in Visits, Dog Walking, Transport, and Attendants. We are veterinary professionals that offer a higher tier level of pet care.

Our tagline is Raising the Bar in Harbortail Animal Care

Require logo to be incorporated

Would like our images used or included

Would like to include that we offer law enforcement and military discounts

www.harbortailkeepers.net is our website
An example of our print marketing materials attached

```html
<!DOCTYPE html>
<html lang="en">
<head>
<meta charset="utf-8">
<title>Harbortail Keepers Florida – Retractable Banner</title>
<link href="https://fonts.googleapis.com/css2?family=Montserrat:wght@300;400;500;600;700;800&family=Allura&display=swap" rel="stylesheet">
<style>
  :root{
    --teal:#4ac3c3;
    --teal-soft:#bfeaea;
    --yellow:#f5b91a;
    --black:#000000;
    --white:#ffffff;
    --ink:#1a1a1a;
    --stage:#e4e4e4;
  }
  *{margin:0;padding:0;box-sizing:border-box;}
  html,body{width:1200px;height:2387px;overflow:hidden;}
  body{background:var(--stage);font-family:"Montserrat",Arial,sans-serif;}

  .banner{position:absolute;left:100px;top:18px;width:1000px;height:2352px;overflow:hidden;background:var(--black);}
  .banner-shapes{position:absolute;left:0;top:0;width:1000px;height:2352px;}

  .centered{position:absolute;left:0;width:100%;text-align:center;}

  .brand-mark{position:absolute;left:455px;top:58px;width:90px;height:90px;border-radius:50%;background:var(--teal);}
  .brand-name{top:160px;color:var(--yellow);font-weight:700;font-size:44px;line-height:50px;letter-spacing:1px;}
  .brand-name .brand-state{display:block;font-size:20px;line-height:24px;letter-spacing:6px;}
  .tagline{top:240px;color:var(--white);font-weight:400;font-size:26px;line-height:34px;letter-spacing:.5px;}

  .script{font-family:"Allura",cursive;color:var(--white);}
  .intro-label{top:330px;font-size:90px;line-height:100px;}
  .headline{top:420px;line-height:66px;}
  .headline .line-teal{display:block;color:var(--teal);font-weight:700;font-size:54px;}
  .headline .line-white{display:block;color:var(--white);font-weight:300;font-size:50px;}
  .headline .line-yellow{display:block;color:var(--yellow);font-weight:700;font-size:54px;}

  .photo{position:absolute;border-radius:50%;border:26px solid var(--teal);}
  .photo-main{left:76px;top:660px;width:848px;height:848px;
    background:linear-gradient(180deg,#7a5a44 0%,#5b4a40 16%,#262a31 30%,#2e3640 46%,#5e9cc8 56%,#7fa9cf 66%,#9a9c9e 80%,#b9b6b2 100%);}
  .photo-left{left:41px;top:1232px;width:376px;height:376px;
    background:linear-gradient(160deg,#e7e1dc 0%,#c9bcb2 35%,#8a6c5a 60%,#d6ccc4 100%);}
  .photo-right{left:583px;top:1232px;width:376px;height:376px;
    background:linear-gradient(135deg,#3f7f2e 0%,#55983d 50%,#2f6a24 100%);}

  .offer-label{top:1545px;font-size:96px;line-height:100px;color:var(--yellow);}
  .discount{top:1636px;font-size:42px;line-height:61px;color:var(--ink);font-weight:700;}
  .discount .light{font-weight:400;}

  .services-title{position:absolute;left:289px;top:1776px;width:413px;height:79px;border-radius:40px;background:var(--black);color:var(--white);font-weight:700;font-size:44px;line-height:79px;text-align:center;letter-spacing:1px;}

  .service{position:absolute;display:flex;align-items:center;color:var(--ink);font-weight:700;font-size:35px;line-height:42px;}
  .service-icon{flex:none;width:70px;height:70px;border-radius:50%;background:var(--teal);border:4px solid var(--teal-soft);margin-right:20px;display:flex;align-items:center;justify-content:center;}
  .service-icon svg{width:38px;height:38px;}
  .svc-overnights{left:104px;top:1887px;}
  .svc-popin{left:506px;top:1887px;}
  .svc-walking{left:104px;top:2017px;}
  .svc-transport{left:506px;top:2010px;}

  .contact-bar{position:absolute;left:54px;top:2229px;width:890px;height:65px;border-radius:33px;background:var(--white);}
  .contact-phone{position:absolute;left:0;top:0;width:440px;height:65px;border-radius:33px 0 0 33px;background:var(--black);display:flex;align-items:center;padding-left:12px;color:var(--white);font-weight:700;font-size:31px;}
  .phone-icon{width:46px;height:46px;border-radius:50%;background:var(--white);display:flex;align-items:center;justify-content:center;margin-right:12px;}
  .globe-icon{position:absolute;left:381px;top:10px;width:45px;height:45px;border-radius:50%;background:var(--yellow);display:flex;align-items:center;justify-content:center;}
  .contact-web{position:absolute;left:470px;top:0;height:65px;line-height:65px;font-size:30px;font-weight:500;color:var(--ink);}
  .contact-web .web-name{color:var(--teal);}
</style>
</head>
<body>
<main class="banner">
  <svg class="banner-shapes" viewBox="0 0 1000 2352" aria-hidden="true">
    <path d="M0,939 Q500,640 1000,925 L1000,2352 L0,2352 Z" fill="var(--white)"/>
    <rect x="0" y="1950" width="1000" height="402" fill="var(--teal)"/>
    <path d="M0,1705 Q500,1830 1000,1705 L1000,2048 Q500,2280 0,2102 Z" fill="var(--yellow)"/>
    <line x1="124" y1="387" x2="358" y2="387" stroke="var(--yellow)" stroke-width="4"/>
    <line x1="645" y1="387" x2="880" y2="387" stroke="var(--yellow)" stroke-width="4"/>
  </svg>

  <div class="brand-mark"></div>
  <div class="centered brand-name">HARBORTAIL KEEPERS<span class="brand-state">FLORIDA</span></div>
  <p class="centered tagline">Raising the Bar in Harbortail Animal Care</p>

  <div class="centered script intro-label">We are</div>
  <h1 class="centered headline">
    <span class="line-teal">Veterinary professionals</span>
    <span class="line-white">that offer a higher tier</span>
    <span class="line-yellow">level of pet care</span>
  </h1>

  <div class="photo photo-main" role="img" aria-label="Photo of a smiling pet sitter sitting on the floor playing with cats in a living room"></div>
  <div class="photo photo-left" role="img" aria-label="Photo of a dog resting on a soft blanket"></div>
  <div class="photo photo-right" role="img" aria-label="Photo of a teal stethoscope lying on green grass"></div>

  <div class="centered script offer-label">We offer</div>
  <p class="centered discount">Law Enforcement <span class="light">and</span><br>Military Discounts</p>

  <div class="services-title">OUR SERVICES</div>

  <div class="service svc-overnights">
    <span class="service-icon"><svg viewBox="0 0 40 40"><path d="M6 20 L20 8 L34 20 M10 17 V33 H30 V17" fill="none" stroke="#fff" stroke-width="3" stroke-linejoin="round"/></svg></span>Overnights
  </div>
  <div class="service svc-popin">
    <span class="service-icon"><svg viewBox="0 0 40 40"><path d="M20 35 C12 25 9 20 9 15 A11 11 0 0 1 31 15 C31 20 28 25 20 35 Z" fill="none" stroke="#fff" stroke-width="3"/><circle cx="20" cy="15" r="4" fill="#fff"/></svg></span>Pop in Visits
  </div>
  <div class="service svc-walking">
    <span class="service-icon"><svg viewBox="0 0 40 40"><path d="M8 32 L14 20 L22 22 M14 20 L12 10 L28 10" fill="none" stroke="#fff" stroke-width="3" stroke-linecap="round" stroke-linejoin="round"/><circle cx="30" cy="28" r="4" fill="#fff"/></svg></span>Dog Walking
  </div>
  <div class="service svc-transport">
    <span class="service-icon"><svg viewBox="0 0 40 40"><path d="M5 27 V14 H25 L33 21 V27 Z" fill="none" stroke="#fff" stroke-width="3" stroke-linejoin="round"/><circle cx="12" cy="29" r="3.5" fill="#fff"/><circle cx="27" cy="29" r="3.5" fill="#fff"/></svg></span>Transport and<br>Attendants
  </div>

  <div class="contact-bar">
    <div class="contact-phone">
      <span class="phone-icon"><svg width="26" height="26" viewBox="0 0 24 24"><path d="M6.6 10.8a15 15 0 0 0 6.6 6.6l2.2-2.2a1 1 0 0 1 1-.25 11.4 11.4 0 0 0 3.6.57 1 1 0 0 1 1 1V20a1 1 0 0 1-1 1A17 17 0 0 1 3 4a1 1 0 0 1 1-1h3.5a1 1 0 0 1 1 1c0 1.25.2 2.45.57 3.570a1 1 0 0 1-.25 1z" fill="#000"/></svg></span>+1 555-014-2290
    </div>
    <span class="globe-icon"><svg width="28" height="28" viewBox="0 0 24 24"><circle cx="12" cy="12" r="9" fill="none" stroke="#000" stroke-width="1.8"/><ellipse cx="12" cy="12" rx="4" ry="9" fill="none" stroke="#000" stroke-width="1.6"/><line x1="3" y1="12" x2="21" y2="12" stroke="#000" stroke-width="1.6"/></svg></span>
    <div class="contact-web">www.<span class="web-name">harbortailkeepers</span>.net</div>
  </div>
</main>
</body>
</html>
```